8x8 Social Media Ad - Harbor Summit Expo

Attention Real Estate Agents
Please join us for our
Quarterly Real Estate Training Expo
The 2nd Saturday of February, May, August and November
Our Next Training Expo is _________________________________
From 9 am to 1 pm
at
Marlowe Suites Fernridge Station
4187 Copperleaf Lane, Ashbury Heights, MD 20999
Scheduled Speakers
9:00 am - Desmond Pryce - Orientation
9:30 am - Terrell Oakes - Multiple Income Streams / Keystone Track
10:00 am - Lorna Beckett - Marketing though Social Media
10:45 am - Raul Denning - Generating Business through Kelp-Nest
11:30 am - Tunde Adesemi - Real Estate Investing
12:15 pm - Marcus Oyelowo - (Main Speaker) Training Topic TBA
For more information call Desmond Pryce at (240) 555-0192 or email dpryce@harborsummithomes.example

```html
<!DOCTYPE html>
<html lang="en">
<head>
<meta charset="utf-8">
<title>Harbor Summit Expo – Quarterly Real Estate Training Expo</title>
<link rel="stylesheet" href="https://fonts.googleapis.com/css2?family=Montserrat:ital,wght@0,300;0,400;0,500;0,600;0,700;0,800;1,300;1,400;1,500;1,700;1,800&display=swap">
<style>
  :root {
    --ink: #0d5c5b;
    --deep: #0e5f5e;
    --panel: #13807d;
    --band: #1fa8a2;
    --cyan: #2ee6dc;
    --yellow: #f5ea1c;
    --white: #ffffff;
    --photo-a: #3a4a52;
    --photo-b: #7f6a5e;
  }
  * { margin: 0; padding: 0; box-sizing: border-box; }
  html, body { width: 1200px; height: 1200px; overflow: hidden; background: var(--white); }
  body { font-family: "Montserrat", sans-serif; color: var(--ink); }
  .ad { position: relative; width: 1200px; height: 1200px; overflow: hidden; background: var(--white); }

  .brand { position: absolute; left: 66px; top: 80px; display: flex; align-items: center; gap: 14px; }
  .brand-mark { width: 34px; height: 34px; background: var(--ink); }
  .brand-name { font-weight: 800; font-size: 40px; color: var(--ink); letter-spacing: 1px; line-height: 1; }

  .feature-band { position: absolute; left: 0; top: 406px; width: 800px; height: 332px; background: var(--band); }

  .headline { position: absolute; left: 74px; top: 196px; font-style: italic; line-height: 1.1; color: var(--ink); }
  .headline .light { font-weight: 400; font-size: 59px; display: block; }
  .headline .strong { font-weight: 800; font-size: 62px; display: block; }

  .invite { position: absolute; left: 46px; top: 344px; width: 582px; height: 72px; }
  .invite svg { position: absolute; inset: 0; }
  .invite p { position: relative; line-height: 72px; padding-left: 34px; font-size: 33px; font-weight: 500; color: var(--ink); }
  .invite b { font-weight: 800; font-style: italic; }

  .event-title { position: absolute; left: 0; width: 680px; top: 452px; text-align: center; font-style: italic; color: var(--white); line-height: 1.0; }
  .event-title span { display: block; }
  .event-title .thin { font-weight: 300; font-size: 68px; }
  .event-title .thin b { font-weight: 800; }
  .event-title .accent { color: var(--yellow); font-weight: 800; font-size: 68px; }

  .schedule-note { position: absolute; left: 40px; width: 600px; top: 752px; text-align: center; font-size: 35px; line-height: 1.16; color: var(--ink); }
  .schedule-note .caps { font-weight: 800; }
  .schedule-note .reg { font-weight: 400; }

  .venue { position: absolute; left: 78px; top: 982px; display: flex; gap: 20px; }
  .venue svg { flex: none; margin-top: 6px; }
  .venue p { font-size: 26px; font-weight: 500; line-height: 1.14; text-transform: uppercase; color: var(--ink); }

  .speaker-panel { position: absolute; left: 750px; top: 36px; width: 450px; height: 1038px; background: var(--panel); border-radius: 72px 0 0 72px; }

  .panel-title { position: absolute; left: 686px; top: 60px; width: 478px; height: 64px; }
  .panel-title svg { position: absolute; inset: 0; }
  .panel-title p { position: relative; text-align: center; line-height: 64px; font-size: 31px; font-weight: 500; color: var(--white); letter-spacing: 0.5px; }
  .panel-title b { color: var(--cyan); font-weight: 800; }

  .speaker { position: absolute; left: 680px; width: 510px; height: 140px; display: flex; align-items: center; gap: 16px; }
  .speaker-photo { flex: none; width: 140px; height: 140px; border-radius: 50%; background: var(--cyan); padding: 8px; }
  .speaker-photo div { width: 100%; height: 100%; border-radius: 50%; background: linear-gradient(160deg, var(--photo-b), var(--photo-a)); }
  .speaker-info { color: var(--white); }
  .speaker-time { font-style: italic; font-weight: 400; font-size: 30px; line-height: 1.15; }
  .speaker-name { font-weight: 800; font-size: 24px; color: var(--cyan); text-transform: uppercase; line-height: 1.3; letter-spacing: 0.3px; }
  .speaker-topic { font-weight: 700; font-size: 17px; text-transform: uppercase; line-height: 1.2; }

  .contact-bar { position: absolute; left: 0; top: 1110px; width: 1200px; height: 90px; background: var(--deep); color: var(--white); display: flex; align-items: center; padding: 0 26px; }
  .contact-lead { font-size: 19px; font-weight: 500; line-height: 1.05; text-transform: uppercase; }
  .contact-phone { display: flex; align-items: center; gap: 6px; margin-left: 12px; font-weight: 800; font-size: 37px; }
  .contact-email { margin-left: auto; text-align: center; font-size: 24px; font-weight: 500; line-height: 1.15; text-transform: uppercase; }
</style>
</head>
<body>
<main class="ad">
  <div class="feature-band"></div>

  <div class="brand">
    <span class="brand-mark"></span>
    <span class="brand-name">HARBOR SUMMIT</span>
  </div>

  <h1 class="headline">
    <span class="light">ATTENTION REAL</span>
    <span class="strong">ESTATE AGENTS</span>
  </h1>

  <div class="invite">
    <svg width="582" height="72" viewBox="0 0 582 72"><polygon points="22,0 582,0 560,72 0,72" fill="var(--yellow)"/></svg>
    <p>PLEASE JOIN <b>US FOR OUR</b></p>
  </div>

  <h2 class="event-title">
    <span class="thin">QUARTERLY</span>
    <span class="thin">REAL <b>ESTATE</b></span>
    <span class="accent">TRAINING</span>
    <span class="accent">EXPO</span>
  </h2>

  <p class="schedule-note">
    <span class="caps">THE 2ND SATURDAY OF<br>FEBRUARY, MAY, AUGUST<br>AND NOVEMBER</span><br>
    <span class="reg">OUR NEXT TRAINING EXPO</span><br>
    <span class="caps">IS FROM 9 AM TO 1 PM</span>
  </p>

  <div class="venue">
    <svg width="32" height="42" viewBox="0 0 30 40" aria-hidden="true"><path d="M15 0C6.7 0 0 6.7 0 15c0 10.5 15 25 15 25s15-14.5 15-25C30 6.7 23.3 0 15 0zm0 21a6 6 0 1 1 0-12 6 6 0 0 1 0 12z" fill="var(--ink)"/></svg>
    <p>At Marlowe Suites Fernridge<br>Station 4187 Copperleaf<br>Lane, Ashbury Heights,<br>MD 20999.</p>
  </div>

  <div class="speaker-panel"></div>

  <div class="panel-title">
    <svg width="478" height="64" viewBox="0 0 478 64"><polygon points="14,0 478,0 464,64 0,64" fill="var(--ink)"/></svg>
    <p>SCHEDULED <b>SPEAKERS</b></p>
  </div>

  <div class="speaker" style="top:158px">
    <div class="speaker-photo" role="img" aria-label="Portrait photo of Desmond Pryce"><div></div></div>
    <div class="speaker-info"><p class="speaker-time">9:00 AM</p><p class="speaker-name">Desmond Pryce</p><p class="speaker-topic">Orientation</p></div>
  </div>
  <div class="speaker" style="top:308px">
    <div class="speaker-photo" role="img" aria-label="Portrait photo of Terrell Oakes"><div></div></div>
    <div class="speaker-info"><p class="speaker-time">9:30 AM</p><p class="speaker-name">Terrell Oakes</p><p class="speaker-topic">Multiple Income<br>Streams / Keystone Track</p></div>
  </div>
  <div class="speaker" style="top:458px">
    <div class="speaker-photo" role="img" aria-label="Portrait photo of Lorna Beckett"><div></div></div>
    <div class="speaker-info"><p class="speaker-time">10:00 AM</p><p class="speaker-name">Lorna Beckett</p><p class="speaker-topic">Marketing<br>Though Social Media</p></div>
  </div>
  <div class="speaker" style="top:608px">
    <div class="speaker-photo" role="img" aria-label="Portrait photo of Raul Denning"><div></div></div>
    <div class="speaker-info"><p class="speaker-time">10:45 AM</p><p class="speaker-name">Raul Denning</p><p class="speaker-topic">Generating Business<br>Through Kelp-Nest</p></div>
  </div>
  <div class="speaker" style="top:758px">
    <div class="speaker-photo" role="img" aria-label="Portrait photo of Tunde Adesemi"><div></div></div>
    <div class="speaker-info"><p class="speaker-time">11:30 AM</p><p class="speaker-name">Tunde Adesemi</p><p class="speaker-topic">Real Estate Investing</p></div>
  </div>
  <div class="speaker" style="top:908px">
    <div class="speaker-photo" role="img" aria-label="Portrait photo of Marcus Oyelowo"><div></div></div>
    <div class="speaker-info"><p class="speaker-time">12:15 PM</p><p class="speaker-name">Marcus Oyelowo</p><p class="speaker-topic">(Main Speaker)<br>Training Topic TBA</p></div>
  </div>

  <footer class="contact-bar">
    <p class="contact-lead">For more information<br>call Desmond Pryce at</p>
    <p class="contact-phone">
      <svg width="32" height="32" viewBox="0 0 30 30" aria-hidden="true"><circle cx="15" cy="15" r="15" fill="var(--white)"/><path d="M10.5 7.5l3 3.2-1.6 2.1c.9 1.9 2.4 3.4 4.3 4.3l2.1-1.6 3.2 3-1.7 2.6c-5.6-.4-11.4-6.2-11.8-11.8z" fill="var(--deep)"/></svg>
      (240) 555-0192
    </p>
    <p class="contact-email">Or email<br>dpryce@harborsummithomes.example</p>
  </footer>
</main>
</body>
</html>
```